Packaging Design Project

I need a box for a hair oil called NEL. 3 color, Simple design .. We are open to new ideas, the over all theme.. Pure and Simple , Natural, Color protect, good for the hair. We started with a basic design and this is the existing website http://nelhaircare.com/

Industry/Entity Type

Hair

```html
<!DOCTYPE html>
<html lang="en">
<head>
<meta charset="utf-8">
<title>NEL Hair Oil – Box Front</title>
<link rel="stylesheet" href="https://fonts.googleapis.com/css2?family=Quicksand:wght@300;500&family=Patrick+Hand&display=swap">
<style>
  :root {
    --page: #ffffff;
    --rust: #a8330c;
    --rust-deep: #952c0a;
    --pattern: #b5471f;
    --sand: #c8976a;
    --sand-pattern: #cfa47b;
    --cream: #efe8cc;
    --brown: #4b2718;
    --white: #fbf3ea;
    --blush: #eba58a;
  }
  * { margin: 0; padding: 0; box-sizing: border-box; }
  html, body { width: 965px; height: 1200px; overflow: hidden; background: var(--page); }
  .canvas { position: relative; width: 965px; height: 1200px; }

  .box-front {
    position: absolute; left: 267px; top: 43px;
    width: 430px; height: 1114px;
    background: var(--rust);
    overflow: hidden;
    font-family: "Quicksand", sans-serif;
    text-align: center;
  }
  .floral-backdrop {
    position: absolute; inset: 0 0 226px 0;
    background: radial-gradient(ellipse at 60% 20%, var(--pattern) 0%, var(--rust) 55%, var(--rust-deep) 100%);
  }

  .brand-plate {
    position: absolute; left: 40px; top: 120px;
    width: 350px; height: 230px;
    background: var(--cream);
    border: 6px solid var(--brown);
    border-radius: 28px;
    display: flex; align-items: center; justify-content: center;
  }
  .brand-name {
    font-family: "Quicksand", sans-serif;
    font-weight: 500;
    font-size: 104px;
    color: var(--brown);
    letter-spacing: 4px;
  }

  .product-title {
    position: absolute; left: 0; right: 0; top: 405px;
    color: var(--white);
    font-weight: 300;
    font-size: 38px;
    line-height: 52px;
  }
  .claims {
    position: absolute; left: 0; right: 0; top: 597px;
    list-style: none;
    color: var(--blush);
    font-weight: 300;
    font-size: 28px;
    line-height: 34.5px;
  }

  .info-band {
    position: absolute; left: 0; right: 0; bottom: 0; height: 226px;
    background: radial-gradient(ellipse at 20% 70%, var(--sand-pattern) 0%, var(--sand) 60%);
  }
  .band-edge { position: absolute; left: 0; top: 0; width: 430px; height: 8px; }
  .benefits {
    position: absolute; left: 20px; right: 20px; top: 40px;
    font-family: "Patrick Hand", cursive;
    color: var(--brown);
    font-size: 27px;
    line-height: 34px;
  }
  .volume {
    position: absolute; left: 0; right: 0; top: 170px;
    color: var(--brown);
    font-weight: 300;
    font-size: 26px;
  }
</style>
</head>
<body>
<div class="canvas">
  <section class="box-front">
    <div class="floral-backdrop" role="img" aria-label="Faint rust-toned floral and botanical pattern"></div>

    <div class="brand-plate">
      <span class="brand-name">NEL</span>
    </div>

    <h1 class="product-title">Protective hair- oil<br>treatment<br>and styling aid</h1>

    <ul class="claims">
      <li>paraben free</li>
      <li>sulfate free</li>
      <li>alergy tested</li>
      <li>alcohol free</li>
    </ul>

    <div class="info-band" role="img" aria-label="Sand-coloured band with faint floral pattern">
      <svg class="band-edge" viewBox="0 0 430 8" aria-hidden="true">
        <rect width="430" height="3" fill="#a8330c"/>
        <line x1="0" y1="5" x2="430" y2="5" stroke="#efe8cc" stroke-width="4" stroke-dasharray="9 3" stroke-linecap="round"/>
      </svg>
      <p class="benefits">style, smooth, shine &amp; condition<br>ALL hair of types while looking in<br>moisture</p>
      <p class="volume">100 ml/ 3.4 oz</p>
    </div>
  </section>
</div>
</body>
</html>
```